Design a landing page

We have a logo, we have colours in mind. What we need is to create a typical one-page landing page that would look nicely on both PC and mobile devices/tablets.

Typical layout - logo top left, top right - shop/client area buttons (links will open to different websites), informational area in the middle - image on the left + text on the right then image on the right + text on the left etc., then text links at the bottom (T&S, Cookie policy, privacy policy etc.).

Page must have cookie notification as per EU law.

We will also need help in preparing photos/images (up to 8) for the website.

End result should be either a Wordpress theme (preferred - so we can install it from wordpress control panel) or HTML/CSS page source. All scripts/images/files should be included - no external links to js/image libraries please.

The photo of the device attached. Primary users will be home users with placement on the ceiling, Minority of users will be business/commercial users with wall placements. Device is meant to monitor climat in the premises (Temperature, humidity, dew point) and alert users if readings are not within allowed range.

Industry/Entity Type

Microclimate Monitoring in premises

Coding

Coded - Design and coding required

Number of Pages Required

1 page

Colors
0054AA
0677BA
7BADD7
CADEEF
E8F1F8
0094D4
00A9DD
6FCCEA
C7EBF8
E9F6FB

Requirements
Must have
• White background, layout as described unless better option offered and accepted. Must have cookie warning.

```html
<!DOCTYPE html>
<html lang="en">
<head>
<meta charset="utf-8">
<title>CLIMORA – Microclimate Monitoring</title>
<link rel="stylesheet" href="https://fonts.googleapis.com/css2?family=Red+Hat+Display:wght@500;600;700&family=Roboto:wght@400;500;700&display=swap">
<style>
:root{
  --navy:#0054AA;
  --navy-deep:#0054AA;
  --blue-mid:#0677BA;
  --teal:#00A9DD;
  --teal-dark:#0094D4;
  --sky:#6FCCEA;
  --grey-bg:#E9F6FB;
  --pale:#E8F1F8;
  --text:#3a3f47;
  --white:#ffffff;
  --head:"Red Hat Display",sans-serif;
  --body:"Roboto",sans-serif;
}
*{box-sizing:border-box;margin:0;padding:0}
html,body{width:1200px;height:4702px;overflow:hidden}
body{background:var(--white);font-family:var(--body);color:var(--text);position:relative}
.abs{position:absolute}
a{text-decoration:none;color:inherit}

/* header */
.site-header{position:absolute;top:0;left:0;width:1200px;height:139px;background:var(--white)}
.brand{position:absolute;font-family:var(--head);font-weight:700;color:var(--navy);font-size:46px;letter-spacing:1px;display:flex;align-items:center;gap:12px}
.brand .dot{width:14px;height:14px;background:var(--teal);border-radius:50%}
.site-header .brand{left:110px;top:44px}
.btn{display:inline-flex;align-items:center;justify-content:center;font-family:var(--body);font-weight:700;font-size:14px;letter-spacing:.3px;text-transform:uppercase;border-radius:3px;color:var(--white);background:var(--teal);position:absolute}
.btn-outline{background:var(--white);color:var(--navy);border:1.5px solid var(--teal);box-shadow:0 2px 4px rgba(0,0,0,.12)}
.btn-navy{background:var(--navy)}
.main-nav{position:absolute;top:99px;left:493px;width:595px;display:flex;justify-content:space-between;font-size:14px;font-weight:500;color:var(--navy);text-transform:uppercase}
.main-nav .active{color:var(--teal);border-bottom:1.5px solid var(--teal);padding-bottom:2px}

/* hero */
.hero{position:absolute;top:139px;left:0;width:1200px;height:640px}
.hero-photo{position:absolute;inset:0;background:linear-gradient(100deg,#5e6d80 0%,#8c96a3 40%,#aeb5bf 70%,#d3d8de 100%)}
.hero-shade{position:absolute;inset:0;background:linear-gradient(90deg,rgba(0,40,90,.55),rgba(0,40,90,0) 55%)}
.hero h1{position:absolute;left:110px;top:108px;font-family:var(--head);font-weight:500;font-size:38px;line-height:46px;color:var(--white)}
.hero p{position:absolute;left:111px;top:210px;width:460px;font-size:17px;line-height:27px;color:var(--white)}
.hero .dots{position:absolute;top:523px;left:560px;display:flex;gap:12px}
.hero .dots span{width:11px;height:11px;border-radius:50%;background:rgba(255,255,255,.55)}
.hero .dots span.on{background:var(--white)}

/* shared */
.section-title{font-family:var(--head);font-weight:500;color:var(--navy);font-size:40px;line-height:47px}
.rule{width:84px;height:2px;background:var(--teal)}
.copy{font-size:14.5px;line-height:24px;text-align:justify}
.photo{position:absolute}
.hex{clip-path:polygon(25% 3%,75% 3%,100% 50%,75% 97%,25% 97%,0 50%);border-radius:40px}

/* bands */
.band-grey{position:absolute;left:0;width:1200px;background:var(--grey-bg)}
.band-teal{position:absolute;left:0;width:1200px;background:var(--teal)}
.band-navy{position:absolute;left:0;width:1200px;background:var(--navy-deep)}

.bullets{list-style:none;font-size:15.5px;color:#222;line-height:34px}
.bullets li::before{content:"";display:inline-block;width:4px;height:4px;border-radius:50%;background:var(--teal);margin:0 14px 3px 2px}

/* cards */
.card-wrap{position:absolute;top:2852px;width:226px;height:247px;filter:drop-shadow(0 3px 6px rgba(0,60,120,.16))}
.card{width:100%;height:100%;background:var(--white);clip-path:polygon(50% 0,100% 18%,100% 82%,50% 100%,0 82%,0 18%);text-align:center;padding-top:48px}
.card svg{width:54px;height:54px}
.card h3{font-size:14px;font-weight:700;color:var(--navy);margin-top:12px}
.card p{font-size:13.5px;line-height:23px;margin:6px 18px 0}

/* footer */
.footer-col{position:absolute;top:4396px}
.footer-col h4{font-size:15px;font-weight:700;color:var(--navy);margin-bottom:16px}
.footer-col li{list-style:none;font-size:13.5px;color:var(--text);height:33px;display:flex;align-items:center;gap:14px}
.footer-col li::before{content:"";width:11px;height:11px;border-radius:50%;background:var(--teal)}
.contact-row{display:flex;gap:18px;margin-bottom:14px;font-size:12.5px;line-height:19px}
.contact-row b{display:block;font-size:14px;color:var(--navy)}
.social{position:absolute;top:4652px;width:28px;height:28px;border-radius:50%;background:var(--pale)}
.social.first{background:var(--teal)}

/* cookie notice */
.cookie-notice{position:absolute;left:110px;top:4560px;width:330px;padding:12px 14px;background:var(--white);border:1px solid #CADEEF;border-left:4px solid var(--teal);border-radius:4px;box-shadow:0 4px 14px rgba(0,84,170,.15);font-size:12px;line-height:17px;color:var(--text)}
.cookie-notice strong{display:block;font-size:13px;color:var(--navy);margin-bottom:3px}
.cookie-actions{display:flex;gap:8px;margin-top:8px}
.cookie-actions span{font-size:11px;font-weight:700;text-transform:uppercase;padding:5px 10px;border-radius:3px}
.cookie-accept{background:var(--teal);color:var(--white)}
.cookie-settings{border:1px solid var(--teal);color:var(--navy)}
</style>
</head>
<body>

<header class="site-header">
  <div class="brand">CLIMORA<span class="dot"></span></div>
  <a class="btn btn-outline" style="left:794px;top:31px;width:141px;height:46px">Shop Now</a>
  <a class="btn" style="left:946px;top:31px;width:142px;height:46px">Client Area</a>
  <nav class="main-nav">
    <a class="active">Home</a><a>About</a><a>Solutions</a><a>Applications</a><a>Resources</a><a>Contact</a>
  </nav>
</header>

<section class="hero">
  <div class="hero-photo" role="img" aria-label="Living room with a family on a sofa and a dark hexagonal climate sensor on the wall"></div>
  <div class="hero-shade"></div>
  <svg class="abs" style="left:0;top:0" width="1200" height="640" viewBox="0 0 1200 640">
    <polygon points="0,354 603,660 1200,376 1200,640 0,640" fill="#fff"/>
    <polygon points="400,558 603,660 1200,376 1200,420 603,632" fill="#00A9DD"/>
    <polygon points="0,380 603,660 1200,420 1200,452 603,690 0,400" fill="#fff"/>
  </svg>
  <h1>STAY IN CONTROL<br>OF YOUR ENVIRONMENT</h1>
  <p>Track conditions in real time and respond before small changes become costly problems.</p>
  <a class="btn" style="left:111px;top:286px;width:143px;height:46px">Get Started</a>
  <div class="dots"><span></span><span class="on"></span><span></span><span></span></div>
</section>

<!-- about -->
<section>
  <div class="abs" style="left:111px;top:955px;width:203px;height:305px;background:var(--teal);border-radius:22px"></div>
  <div class="photo" style="left:137px;top:882px;width:398px;height:356px;border-radius:18px;background:linear-gradient(90deg,#ececec 0%,#e2e2e2 38%,#b8322d 40%,#8d2a2a 55%,#33475f 75%,#1e2a3a 100%)" role="img" aria-label="Dark hexagonal sensor mounted on a white brick wall beside red storage cabinets in a warehouse"></div>
  <h2 class="section-title abs" style="left:625px;top:876px">ABOUT CLIMORA</h2>
  <div class="rule abs" style="left:625px;top:925px"></div>
  <div class="abs copy" style="left:625px;top:954px;width:464px">
    <p>CLIMORA delivers intelligent microclimate monitoring systems for commercial, technical, and controlled environments. Our technology continuously measures critical parameters such as temperature, humidity, and air quality to ensure stable and compliant indoor conditions.</p>
    <p style="margin-top:10px;text-align:left">Built for reliability and ease of use, our systems provide clear insights that help teams make fast, informed decisions.</p>
  </div>
  <a class="btn" style="left:625px;top:1169px;width:142px;height:44px">Learn More</a>
</section>

<!-- continuous tracking -->
<section class="band-grey" style="top:1366px;height:643px">
  <h2 class="section-title abs" style="left:111px;top:78px">CONTINUOUS<br>ENVIRONMENTAL<br>TRACKING</h2>
  <div class="rule abs" style="left:111px;top:222px"></div>
  <p class="abs copy" style="left:111px;top:243px;width:484px">CLIMORA records environmental data around the clock, ensuring you always have an accurate view of your space. Measurements are captured in real time and securely stored, allowing you to review both current conditions and long-term trends.</p>
  <ul class="bullets abs" style="left:111px;top:354px">
    <li>Detect fluctuations early</li>
    <li>Identify patterns over time</li>
    <li>Maintain optimal indoor conditions</li>
    <li>Support compliance requirements</li>
  </ul>
  <a class="btn" style="left:111px;top:517px;width:143px;height:44px">Learn More</a>
  <div class="photo hex" style="left:656px;top:89px;width:432px;height:466px;background:linear-gradient(180deg,#d9a93a 0%,#c8952c 38%,#2a2a25 45%,#e2c530 50%,#9aa6b8 62%,#c9cfd8 100%)" role="img" aria-label="White hexagonal sensor above a hazard-striped beam in a warehouse stacked with pallets"></div>
</section>

<!-- alerts -->
<section class="band-teal" style="top:2009px;height:675px">
  <svg class="abs" style="left:0;top:581px" width="1200" height="94" viewBox="0 0 1200 94"><polygon points="0,94 603,0 1200,94" fill="#fff"/></svg>
  <div class="photo hex" style="left:111px;top:82px;width:433px;height:465px;background:linear-gradient(160deg,#e7e4df 0%,#d8d3cb 45%,#b8afa3 100%)" role="img" aria-label="Hand mounting a white sensor on a ceiling next to a pendant lamp"></div>
  <h2 class="section-title abs" style="left:604px;top:111px;color:var(--white)">INSTANT ALERTS<br>WHEN IT MATTERS<br>MOST</h2>
  <div class="rule abs" style="left:604px;top:255px;background:var(--white)"></div>
  <div class="abs copy" style="left:604px;top:281px;width:485px;color:var(--white)">
    <p>Environmental changes can happen quickly. CLIMORA notifies you immediately when readings move outside your defined limits. Instead of discovering problems too late, you receive alerts that allow you to act promptly and avoid potential damage or disruption.</p>
    <p style="margin-top:10px">Notifications are delivered directly to you through your preferred channels, ensuring you stay informed wherever you are.</p>
  </div>
  <a class="btn btn-navy" style="left:604px;top:467px;width:143px;height:46px">Learn More</a>
</section>

<!-- trusted -->
<section>
  <h2 class="section-title abs" style="left:0;top:2723px;width:1200px;text-align:center">TRUSTED ACROSS CRITICAL<br>ENVIRONMENTS</h2>
  <div class="rule abs" style="left:558px;top:2818px"></div>
  <svg class="abs" style="left:40px;top:2960px" width="22" height="32" viewBox="0 0 22 32"><path d="M17 3 5 16l12 13" fill="none" stroke="#CADEEF" stroke-width="4"/></svg>
  <svg class="abs" style="left:1137px;top:2960px" width="22" height="32" viewBox="0 0 22 32"><path d="M5 3l12 13L5 29" fill="none" stroke="#0054AA" stroke-width="4"/></svg>

  <div class="card-wrap" style="left:111px"><div class="card">
    <svg viewBox="0 0 54 54"><rect x="12" y="6" width="30" height="44" fill="#00A9DD"/><g fill="#fff"><rect x="17" y="16" width="5" height="5"/><rect x="25" y="16" width="5" height="5"/><rect x="33" y="16" width="5" height="5"/><rect x="17" y="26" width="5" height="5"/><rect x="25" y="26" width="5" height="5"/><rect x="33" y="26" width="5" height="5"/><rect x="23" y="38" width="8" height="12"/></g></svg>
    <h3>LABORATORIES</h3><p>Lorem ipsum dolor sit amet consectetur adipiscing elit, sed do eiusmea.</p></div></div>
  <div class="card-wrap" style="left:362px"><div class="card">
    <svg viewBox="0 0 54 54"><rect x="8" y="8" width="38" height="26" rx="2" fill="#00A9DD"/><rect x="13" y="13" width="28" height="16" fill="#fff"/><rect x="24" y="34" width="6" height="8" fill="#00A9DD"/><rect x="14" y="42" width="26" height="5" fill="#00A9DD"/></svg>
    <h3>TECHNICAL ROOMS</h3><p>Lorem ipsum dolor sit amet consectetur adipiscing elit, sed do eiusmea.</p></div></div>
  <div class="card-wrap" style="left:612px"><div class="card">
    <svg viewBox="0 0 54 54"><path d="M4 20 27 6l23 14v28H4z" fill="#00A9DD"/><rect x="15" y="28" width="24" height="20" fill="#fff"/><rect x="18" y="36" width="8" height="8" fill="#00A9DD"/><rect x="28" y="36" width="8" height="8" fill="#00A9DD"/></svg>
    <h3>STORAGE FACILITIES</h3><p>Lorem ipsum dolor sit amet consectetur adipiscing elit, sed do eiusmea.</p></div></div>
  <div class="card-wrap" style="left:862px"><div class="card">
    <svg viewBox="0 0 54 54"><rect x="8" y="12" width="6" height="18" fill="#00A9DD"/><path d="M8 30h40V18l-8 5v-5l-8 5v-5l-8 5v7H8z" fill="#00A9DD"/><circle cx="27" cy="42" r="7" fill="none" stroke="#00A9DD" stroke-width="4"/></svg>
    <h3>INDUSTRIAL SPACES</h3><p>Lorem ipsum dolor sit amet consectetur adipiscing elit, sed do eiusmea.</p></div></div>

  <a class="btn" style="left:502px;top:3139px;width:194px;height:46px">Shop Our Product</a>
</section>

<!-- why -->
<section class="band-grey" style="top:3281px;height:585px">
  <h2 class="section-title abs" style="left:111px;top:120px">WHY CLIMORA?</h2>
  <div class="rule abs" style="left:111px;top:170px"></div>
  <div class="abs copy" style="left:111px;top:196px;width:464px">
    <p>Lorem ipsum dolor sit amet, consectetur adipiscing elit, sed do eiusmod tempor incididunt ut labore et dolore magna aliqua. Ut enim ad minim veniam, quis nostrud exercitation ullamco laboris nisi ut aliquip ex ea consequat.</p>
    <p style="margin-top:10px">Duis aute irure dolor in reprehenderit in voluptate velit esse cillum dolore eu fugiat nulla pariatur. Excepteur sint occaecat cupidatat non proidentea.</p>
  </div>
  <a class="btn" style="left:111px;top:413px;width:143px;height:44px">Learn More</a>
  <div class="abs" style="left:884px;top:199px;width:204px;height:309px;background:var(--teal);border-radius:22px"></div>
  <div class="photo" style="left:663px;top:125px;width:401px;height:360px;border-radius:18px;background:linear-gradient(90deg,#f0efed 0%,#e4e2df 40%,#4a3a30 44%,#3b2d24 48%,#dfe4ea 52%,#bcc9d6 100%)" role="img" aria-label="Black hexagonal sensor on a white wall beside a doorway into an office lounge"></div>
</section>

<!-- cta -->
<section class="band-navy" style="top:3866px;height:507px">
  <svg class="abs" style="left:0;top:450px" width="1200" height="57" viewBox="0 0 1200 57"><polygon points="0,0 603,57 0,57" fill="#fff"/><polygon points="1200,0 603,57 1200,57" fill="#fff"/></svg>
  <h2 class="section-title abs" style="left:491px;top:100px;color:var(--white)">TAKE CONTROL OF YOUR<br>INDOOR CLIMATE</h2>
  <p class="abs" style="left:491px;top:213px;width:600px;font-size:15px;line-height:26px;color:var(--white)">Monitor critical environmental conditions in real time and protect your facilities with reliable, automated alerts.</p>
  <a class="btn" style="left:491px;top:285px;width:152px;height:46px">Get Started</a>
</section>

<!-- footer -->
<footer>
  <div class="brand" style="left:110px;top:4486px">CLIMORA<span class="dot"></span></div>
  <div class="footer-col" style="left:469px">
    <h4>QUICK LINKS</h4>
    <ul><li>Home</li><li>About Us</li><li>Solutions</li><li>Applications</li><li>Resources</li><li>Contact Us</li></ul>
  </div>
  <div class="footer-col" style="left:643px">
    <h4>OTHER LINKS</h4>
    <ul><li>Terms &amp; Conditions</li><li>Privacy Policy</li><li>Cookie Policy</li><li>Imprint</li><li>Contact</li></ul>
  </div>
  <div class="footer-col" style="left:862px">
    <h4>CONTACT INFO</h4>
    <div class="contact-row"><svg width="12" height="16" viewBox="0 0 12 16"><path d="M6 0a6 6 0 0 1 6 6c0 4-6 10-6 10S0 10 0 6a6 6 0 0 1 6-6z" fill="#00A9DD"/><circle cx="6" cy="6" r="2" fill="#fff"/></svg><div><b>ADDRESS:</b>465, Lorum Ipsum Dolore Sed Amet,<br>United State</div></div>
    <div class="contact-row"><svg width="14" height="14" viewBox="0 0 14 14"><path d="M3 0l3 3-2 2a8 8 0 0 0 5 5l2-2 3 3-2 3C6 14 0 8 0 3z" fill="#00A9DD"/></svg><div><b>PHONE:</b>+1 (888) 888 8888</div></div>
    <div class="contact-row"><svg width="14" height="11" viewBox="0 0 14 11"><rect width="14" height="11" fill="#00A9DD"/><path d="M0 0l7 6 7-6" fill="none" stroke="#fff" stroke-width="1.4"/></svg><div><b>EMAIL:</b>info@climora.com</div></div>
  </div>

  <div class="cookie-notice" role="dialog" aria-label="Cookie consent">
    <strong>We use cookies</strong>
    This site uses cookies to improve your experience. See our Cookie Policy.
    <div class="cookie-actions"><span class="cookie-accept">Accept</span><span class="cookie-settings">Settings</span></div>
  </div>

  <div class="abs" style="left:111px;top:4640px;width:977px;height:1px;background:#CADEEF"></div>
  <p class="abs" style="left:0;top:4657px;width:1200px;text-align:center;font-size:12.5px">© 2026 CLIMORA &nbsp;·&nbsp; All Rights Reserved</p>
  <span class="social first" style="left:985px"></span>
  <span class="social" style="left:1021px"></span>
  <span class="social" style="left:1058px"></span>
</footer>

</body>
</html>
```